Tallowin Reach Coffee Product Catalogue 2020

8 page catalogue required
Page 1 Cover Page - TRC logo
Page 2 Coffee/Vending/Powdered - stock image of coffee
Page 3 Syrups - Brindle beverages logo
Page 4 Barista Equipment/Brewing - Kavlin Press logo, vosku
Page 5 Takeaway cups/lids - custom Cup logo, Pellow Cup logo
Page 6 Tea - the Quiet Kettlehouse logo
Page 7 Equipment and Water filtration - Clarvon, Vintaro, TKR, Nexlo, Il Trevanto and Copper Ladle Logos. I need some text space to add a blurb later.
Page 8 Contact Details

all products details on attached Xcel file

Target Market(s)

Local market

Font styles to use
Serif

Colors

Designer to choose colors to be used in the design.

Requirements
Must have
• Page 1 Cover Page - TRC logo
• Page 2 Coffee/Vending/Powdered - stock image of coffee beans.
• Page 3 Syrups - Brindle beverages logo
• Page 4 Barista Equipment/Brewing - Kavlin Press logo, vosku
• Page 5 Takeaway cups/lids - custom Cup logo, Pellow Cup logo
• Page 6 Tea - the Quiet Kettlehouse logo
• Page 7 Equipment and Water filtration - Clarvon, Vintaro, TKR, Nexlo, Il Trevanto and Copper Ladle Logos
• Page 8 Contact Details
• all products details on attached Xcel file
Nice to have
• Industrial feel and look
Should not have
• to much colour

```html
<!DOCTYPE html>
<html lang="en">
<head>
<meta charset="utf-8">
<title>Tallowin Reach Coffee – Product Catalogue 2020</title>
<link href="https://fonts.googleapis.com/css2?family=Playfair+Display:ital,wght@0,400;0,700;0,800;1,400&display=swap" rel="stylesheet">
<style>
  :root {
    --paper: #ffffff;
    --ink: #3a2219;
    --mark: #1c1614;
    --bean-dark: #5a3420;
    --bean-mid: #8a5636;
    --bean-light: #a87050;
  }
  html, body {
    margin: 0;
    padding: 0;
    overflow: hidden;
    background: var(--paper);
  }
  .cover {
    position: relative;
    width: 733px;
    height: 1200px;
    background: var(--paper);
    overflow: hidden;
    font-family: "Playfair Display", Georgia, serif;
    color: var(--ink);
  }
  .cover__art {
    position: absolute;
    inset: 0;
  }
  .tagline {
    font-family: "Playfair Display", Georgia, serif;
    font-style: italic;
    font-size: 19px;
    fill: var(--ink);
    letter-spacing: 0.3px;
  }
  .brand {
    position: absolute;
    left: 389px;
    top: 48px;
    width: 283px;
    text-align: center;
  }
  .brand__dot {
    width: 150px;
    height: 150px;
    border-radius: 50%;
    background: var(--mark);
    margin: 0 auto 16px;
  }
  .brand__name {
    margin: 0;
    font-weight: 800;
    font-size: 28px;
    line-height: 1.15;
    color: var(--mark);
    letter-spacing: 1px;
    text-transform: uppercase;
  }
  .title {
    position: absolute;
    right: 56px;
    top: 426px;
    margin: 0;
    text-align: right;
    font-weight: 700;
    font-size: 88px;
    line-height: 112px;
    color: var(--ink);
  }
  .title span { display: block; }
  .subtitle {
    position: absolute;
    right: 62px;
    top: 683px;
    margin: 0;
    font-weight: 400;
    font-size: 27px;
    letter-spacing: 1.2px;
    word-spacing: 8px;
    color: var(--ink);
  }
  .year {
    position: absolute;
    right: 62px;
    top: 782px;
    margin: 0;
    font-weight: 700;
    font-size: 80px;
    line-height: 1;
    color: var(--ink);
  }
</style>
</head>
<body>
<main class="cover">
  <svg class="cover__art" width="733" height="1200" viewBox="0 0 733 1200">
    <defs>
      <linearGradient id="bean-tone" x1="0" y1="0" x2="1" y2="1">
        <stop offset="0" stop-color="var(--bean-mid)"/>
        <stop offset="0.45" stop-color="var(--bean-dark)"/>
        <stop offset="1" stop-color="var(--bean-light)"/>
      </linearGradient>
      <path id="tagline-curve" d="M148,350 C170,230 230,140 320,82"/>
    </defs>
    <path role="img" aria-label="Photograph of roasted coffee beans spilling in a curved wave down the left side and across the bottom"
          fill="url(#bean-tone)"
          d="M0,0 L361,0 C330,40 300,80 271,113 C225,160 180,200 152,226 C135,280 128,310 130,339 C122,400 116,430 118,451 C120,510 125,540 130,564 C150,620 165,650 186,677 C220,730 245,765 271,790 C290,810 300,830 316,846 C350,875 370,890 395,903 C430,930 455,945 480,959 C520,985 550,1000 576,1016 C620,1040 650,1058 677,1072 C700,1085 720,1098 733,1106 L733,1200 L0,1200 Z"/>
    <text class="tagline"><textPath href="#tagline-curve">your bean to cup specialists</textPath></text>
  </svg>

  <header class="brand">
    <div class="brand__dot"></div>
    <p class="brand__name">Tallowin Reach<br>Coffee</p>
  </header>

  <h1 class="title"><span>Product</span><span>Catalogue</span></h1>
  <p class="subtitle">WHOLESALE PRICE LIST</p>
  <p class="year">2020</p>
</main>
</body>
</html>
```